Vantrell Law Letterhead

We need a new letterhead design for a Law Firm. The address for the law firm is 4817 Larkspur Boulevard, Suite 250, Houston, Texas 77342. Phone Number: 832-619-3057; Fax Number: 832-407-1694. The logo is uploaded to the project.

```html
<!DOCTYPE html>
<html lang="en">
<head>
<meta charset="utf-8">
<title>Vantrell Law Stationery</title>
<link href="https://fonts.googleapis.com/css2?family=Open+Sans:wght@400;600&display=swap" rel="stylesheet">
<style>
  :root{
    --navy:#1f2e5c;
    --red:#c8202f;
    --ink:#2b2b2b;
    --muted:#555a63;
    --paper:#ffffff;
    --bg:#ececec;
    --rule:#b9bcc4;
  }
  *{margin:0;padding:0;box-sizing:border-box}
  html,body{width:1200px;height:833px;overflow:hidden;background:var(--bg);font-family:"Open Sans",Arial,sans-serif;color:var(--ink)}
  .canvas{position:relative;width:1200px;height:833px}

  .brand{display:flex;align-items:center;gap:6px;color:var(--navy);font-weight:600;white-space:nowrap}
  .brand-dot{border-radius:50%;background:var(--navy);flex:none}

  .contact-list{list-style:none;color:var(--muted)}
  .contact-list li{display:flex;align-items:center;gap:3px;white-space:nowrap}
  .contact-list svg{flex:none;fill:var(--navy)}

  /* Letterhead */
  .letterhead{position:absolute;left:40px;top:57px;width:495px;height:696px;background:var(--paper);overflow:hidden}
  .letterhead-swoosh{position:absolute;left:0;top:0;width:495px;height:48px}
  .letterhead-header{position:absolute;left:27px;top:98px;right:12px;display:flex;align-items:flex-start}
  .letterhead-header .brand{font-size:19px;margin-top:4px}
  .letterhead-header .brand-dot{width:30px;height:30px}
  .letterhead-address{margin-left:auto;border-left:1px solid var(--rule);padding-left:7px;font-size:7.3px;line-height:10px;color:var(--muted);width:117px}
  .letterhead-header .contact-list{border-left:1px solid var(--rule);padding-left:6px;margin-left:8px;font-size:7.3px;line-height:10.5px}
  .letter-body{position:absolute;left:27px;top:142px;width:449px}
  .letter-salutation{color:var(--navy);font-weight:600;font-size:9px;margin-bottom:14px}
  .letter-body p{font-size:7.25px;line-height:11.7px;margin-bottom:12px;text-align:justify;color:var(--ink)}
  .letter-closing{position:absolute;left:25px;top:404px;font-size:7.5px}
  .letter-signature{position:absolute;left:24px;top:438px;width:106px;height:34px;background:linear-gradient(90deg,#3a3a3a22,#3a3a3a10);border-radius:3px}
  .letter-signer{position:absolute;left:25px;top:477px;font-size:10.5px;color:var(--ink)}
  .letterhead-footer{position:absolute;left:0;right:0;bottom:14px;text-align:center;font-size:9.8px;color:var(--ink)}
  .letterhead-bar{position:absolute;left:0;right:0;bottom:0;height:7px;background:var(--navy);border-top:2px solid var(--red)}

  /* Envelope */
  .envelope{position:absolute;left:608px;top:62px;width:535px;height:268px;background:var(--paper)}
  .envelope .brand{position:absolute;left:22px;top:20px;font-size:23px}
  .envelope .brand-dot{width:36px;height:36px}
  .envelope .contact-list{position:absolute;left:22px;top:206px;border-left:1px solid var(--rule);padding-left:5px;font-size:7.8px;line-height:10.6px}

  /* Cards */
  .card{position:absolute;top:400px;width:198px;height:128px;background:var(--paper)}
  .card-front{left:608px;display:flex;align-items:center;justify-content:center}
  .card-front .brand{font-size:18px}
  .card-front .brand-dot{width:28px;height:28px}
  .card-back{left:880px;text-align:center}
  .card-back .brand{justify-content:center;margin-top:10px;font-size:12.5px}
  .card-back .brand-dot{width:19px;height:19px}
  .card-name{margin-top:14px;font-size:12.5px;letter-spacing:.3px;color:var(--ink)}
  .card-title{font-size:7.5px;font-weight:600;margin-top:5px;padding-top:5px;position:relative}
  .card-title::before{content:"";position:absolute;left:85px;top:0;width:28px;height:1px;background:var(--ink)}
  .card-back .contact-list{margin-top:9px;font-size:4.3px;line-height:6px;display:flex;flex-direction:column;align-items:center}
</style>
</head>
<body>
<main class="canvas">

  <article class="letterhead">
    <svg class="letterhead-swoosh" viewBox="0 0 495 48" preserveAspectRatio="none" aria-hidden="true">
      <path d="M0 0 H495 V42 C360 20 170 8 0 8 Z" fill="var(--navy)"/>
      <path d="M0 3 C170 3 360 16 495 43 L495 45 C360 20 170 9 0 8 Z" fill="var(--red)"/>
    </svg>

    <header class="letterhead-header">
      <div class="brand"><span class="brand-dot"></span>Vantrell Law</div>
      <address class="letterhead-address">4817 Larkspur Boulevard, Suite 250, Houston, Texas 77342</address>
      <ul class="contact-list">
        <li><svg width="6" height="6" viewBox="0 0 10 10"><path d="M2 0 L4 3 L3 4 C4 6 5 7 6 7 L7 6 L10 8 L8 10 C4 10 0 6 0 2 Z"/></svg>832-619-3057</li>
        <li><svg width="6" height="6" viewBox="0 0 10 10"><rect x="1" y="3" width="8" height="5" rx="1"/><rect x="3" y="0" width="4" height="3"/></svg>832-407-1694</li>
        <li><svg width="6" height="6" viewBox="0 0 10 10"><circle cx="5" cy="5" r="4.5"/></svg>www.vantrellinjury.com</li>
      </ul>
    </header>

    <section class="letter-body">
      <h2 class="letter-salutation">LOREM IPSUM,</h2>
      <p>Lorem ipsum dolor sit amet, consectetur adipiscing elit. Donec orci purus, luctus vitae dignissim eu, iaculis sed purus. Vivamus faucibus, ipsum nec aliquet viverra, leo mauris condimentum ligula, sit amet sagittis enim ligula quis arcu. Nam egestas tortor id nisi porttitor mattis. In tortor ante, ultricies in suscipit a, tempus non massa. Vivamus et auctor mi. Fusce vel massa nulla. Phasellus nec eros mauris, et scelerisque orci.</p>
      <p>Donec malesuada orci vitae nulla accumsan porta a id massa. Quisque accumsan iaculis magna sit amet fringilla. Maecenas consequat, magna eget tincidunt semper, odio nibh rutrum mi, id feugiat ante nisi eu risus. Vestibulum nunc orci, rhoncus a placerat in, ultricies in mi. Quisque scelerisque sagittis nulla at porttitor. Donec malesuada orci vitae nulla accumsan porta a id massa. Quisque accumsan iaculis magna sit amet fringilla. Maecenas consequat, magna eget tincidunt semper, odio nibh rutrum mi, id feugiat ante nisi eu risus. Vestibulum nunc orci, rhoncus a placerat in, ultricies in mi. Cras mattis varius eros, vel fringilla nisi suscipit eget. Quisque scelerisque sagittis nulla at porttitor.</p>
      <p>Sed id augue vitae urna euismod commodo aliquet a quam. Pellentesque arcu velit, cursus et malesuada ut, consequat et diam. Nullam erat sem, rhoncus id ullamcorper vitae, rhoncus et arcu. In ultricies ultricies nulla, ut rutrum nisi iaculis at. Donec eu magna a metus ornare faucibus. Fusce aliquet faucibus ultricies. Morbi semper, est id tincidunt gravida, sem arcu adipiscing lacus, ac bibendum nulla leo eu purus. Quisque nec diam sed risus consectetur a ccumsan quis quis nibh. Vestibulum id purus lorem.</p>
    </section>

    <p class="letter-closing">Sincerely,</p>
    <div class="letter-signature" role="img" aria-label="Handwritten signature"></div>
    <p class="letter-signer">Company Director</p>

    <footer class="letterhead-footer">Houston Personal Injury Attorney</footer>
    <div class="letterhead-bar"></div>
  </article>

  <section class="envelope">
    <div class="brand"><span class="brand-dot"></span>Vantrell Law</div>
    <ul class="contact-list">
      <li><svg width="6" height="6" viewBox="0 0 10 10"><path d="M2 0 L4 3 L3 4 C4 6 5 7 6 7 L7 6 L10 8 L8 10 C4 10 0 6 0 2 Z"/></svg>832-619-3057</li>
      <li><svg width="6" height="6" viewBox="0 0 10 10"><rect x="1" y="3" width="8" height="5" rx="1"/><rect x="3" y="0" width="4" height="3"/></svg>832-407-1694</li>
      <li><svg width="6" height="6" viewBox="0 0 10 10"><circle cx="5" cy="5" r="4.5"/></svg>www.vantrellinjury.com</li>
      <li><svg width="6" height="7" viewBox="0 0 10 12"><path d="M5 0 C8 0 10 2 10 5 C10 8 5 12 5 12 C5 12 0 8 0 5 C0 2 2 0 5 0 Z"/></svg>4817 Larkspur Boulevard, Suite 250, Houston, Texas 77342</li>
    </ul>
  </section>

  <section class="card card-front">
    <div class="brand"><span class="brand-dot"></span>Vantrell Law</div>
  </section>

  <section class="card card-back">
    <div class="brand"><span class="brand-dot"></span>Vantrell Law</div>
    <h3 class="card-name">ELLIOT R. VANTRELL</h3>
    <p class="card-title">ATTORNEY</p>
    <ul class="contact-list">
      <li>832-619-3057</li>
      <li>832-407-1694</li>
      <li>www.vantrellinjury.com</li>
      <li>4817 Larkspur Boulevard, Suite 250, Houston, Texas 77342</li>
    </ul>
  </section>

</main>
</body>
</html>
```